Produkt-Etiketten-Design für Wagyu-Bolognese-Sauce
Sehr schnell, sehr hilfsbereit und Änderungen sehr schnell umgesetzt...verdient die 5 Sterne
Zielgruppe
Wir sind ein landwirtschaftliches Unternehmen und züchten Wagyu Rinder und betreiben einen Online Shop.
Unsere Produktpallete beinhaltet Tk und frisch Fleisch und nun wollen wir unser Palette um Convinienc Food erweitern und dafür brauchen wir Etiketten.
Aufgabenstellung
Es sollte optisch zu unserem webauftritt und unserer Linie passen.
Wir brauchen Produkt Etikett für Wagyu Bolognese Sauce.
Gläser Maße hier entnehmen - https://www.vorratika.com/rundglas-435ml-klarglas-rtx.-bq17-kiste-64stk.html
Wir bauchen auch eine Zutaten-und Nährwerttabelle

```html
<!DOCTYPE html>
<html lang="de">
<head>
<meta charset="utf-8">
<title>Wagyu-Sauce alla Bolognese – Etikett</title>
<link rel="stylesheet" href="https://fonts.googleapis.com/css2?family=Arimo:wght@400;700&family=Montserrat:wght@400;600&family=Oswald:wght@300;500&display=swap">
<style>
  :root {
    --brand-red: #a50d29;
    --logo-red: #b5122e;
    --ink: #333333;
    --ink-soft: #555555;
    --ink-light: #6a6a6a;
    --panel-grey: #e6e6e6;
    --row-grey: #b3b3b3;
    --label-white: #ffffff;
    --page: #ffffff;
  }
  * { box-sizing: border-box; margin: 0; padding: 0; }
  html, body { width: 1200px; height: 1146px; overflow: hidden; background: var(--page); }
  .canvas { position: relative; width: 1200px; height: 1146px; }

  /* neck strip */
  .neck-strip {
    position: absolute; left: 527px; top: 152px; width: 87px; height: 223px;
    background: var(--label-white); box-shadow: 0 0 0 1px #eeeeee;
    font-family: "Oswald", sans-serif; font-weight: 300; color: #777;
    font-size: 9.5px; line-height: 13px; text-align: center;
  }
  .neck-strip .mark {
    display: block; margin: 46px auto 6px; width: 34px; height: 34px;
    border: 2.5px solid var(--logo-red); border-radius: 50%;
  }
  .neck-strip .mark + .mark, .neck-strip .claim + .mark { margin-top: 14px; }

  /* main label */
  .label-band {
    position: absolute; left: 33px; top: 394px; width: 1071px; height: 410px;
    background: var(--label-white);
  }
  .label-band .rule-top {
    position: absolute; left: 0; top: 0; width: 100%; height: 16px; background: var(--brand-red);
  }
  .label-band .title-bar {
    position: absolute; left: 0; bottom: 0; width: 100%; height: 54px; background: var(--brand-red);
    display: flex; align-items: center; justify-content: center;
    font-family: "Oswald", sans-serif; font-weight: 500; color: #fff;
    font-size: 38px; letter-spacing: -0.5px; transform-origin: center;
  }
  .title-bar .small { font-size: 25px; margin: 6px 8px 0; }

  .center-panel {
    position: absolute; left: 308px; top: 16px; width: 348px; height: 340px;
    background: linear-gradient(90deg, var(--panel-grey) 0%, #f0f0f0 30%, #f6f6f6 60%, var(--panel-grey) 100%);
  }
  .brand-name {
    position: absolute; left: 308px; top: 16px; width: 348px; text-align: center;
    font-family: "Montserrat", sans-serif; font-weight: 600; font-size: 38px;
    color: var(--logo-red); letter-spacing: 0.5px; line-height: 54px;
  }
  .cattle-illustration {
    position: absolute; left: 372px; top: 59px; width: 302px; height: 297px;
    background: radial-gradient(ellipse at 50% 50%, #d2d2d2 0%, #e2e2e2 55%, rgba(240,240,240,0) 75%);
  }

  /* left column */
  .info-left { position: absolute; left: 15px; top: 24px; width: 278px; font-family: "Arimo", sans-serif; color: var(--ink); text-align: center; }
  .info-left .tagline { font-weight: 700; font-size: 16.5px; line-height: 21px; }
  .info-left .ingredients { margin-top: 18px; font-size: 14px; line-height: 18px; color: var(--ink-soft); }
  .info-left .ingredients strong { color: var(--ink); }

  .nutrition {
    position: absolute; left: 48px; top: 174px; width: 277px;
    border-collapse: collapse; font-family: "Arimo", sans-serif; font-size: 13.5px; color: var(--ink);
  }
  .nutrition th {
    background: var(--row-grey); font-weight: 700; font-size: 14px; height: 17px; line-height: 17px; text-align: center;
  }
  .nutrition td { height: 17px; line-height: 17px; padding: 0; }
  .nutrition td.value { text-align: right; }
  .nutrition tr.shaded td { background: var(--row-grey); }
  .nutrition td.indent { padding-left: 8px; }

  /* right column */
  .info-right { position: absolute; left: 790px; top: 24px; width: 257px; font-family: "Montserrat", sans-serif; color: var(--ink-light); text-align: center; }
  .info-right .best-before { font-weight: 600; font-size: 17px; line-height: 21px; }
  .info-right .batch { margin-top: 21px; font-weight: 600; font-size: 17px; line-height: 21px; }
  .info-right .storage { margin-top: 20px; font-size: 17px; line-height: 21px; }
  .info-right .volume { margin-top: 36px; font-weight: 600; font-size: 30px; line-height: 36px; color: var(--ink-soft); }
  .info-right .producer { margin-top: 39px; font-size: 17px; line-height: 21px; }
</style>
</head>
<body>
<div class="canvas">

  <aside class="neck-strip">
    <span class="mark"></span>
    <p class="claim">Nur sicheres<br>und gesundes Futter</p>
    <span class="mark"></span>
    <p class="claim">Artgerechte<br>Haltung, natürliche<br>Aufzucht</p>
  </aside>

  <section class="label-band">
    <div class="rule-top"></div>
    <div class="center-panel"></div>
    <div class="brand-name">BERGHOF FARM</div>
    <div class="cattle-illustration" role="img" aria-label="Grau gezeichneter Rinderkopf als Linienillustration"></div>

    <div class="info-left">
      <p class="tagline">Leckere Sauce nach Bologneser Art aus sonnengereiften Tomaten und reichlichem Fleischanteil vom Wagyu-Rind</p>
      <p class="ingredients"><strong>Zutaten:</strong> Weiches Quellwasser, Sojaboh-<br>nen, Weizen, Meersalz, Aspergillus</p>
    </div>

    <table class="nutrition">
      <tr><th colspan="2">Durchschnittsnährwerte pro 100ml</th></tr>
      <tr><td>Brennwert</td><td class="value">111 kcal/470kj</td></tr>
      <tr class="shaded"><td>Fett</td><td class="value">0,1g</td></tr>
      <tr><td class="indent">davon ungesättigte</td><td class="value">0,1 g</td></tr>
      <tr class="shaded"><td>Fettsäuren</td><td class="value">0,1g</td></tr>
      <tr><td>Kohlenhydrate</td><td class="value">4,5g</td></tr>
      <tr class="shaded"><td class="indent">davon Zucker</td><td class="value">1,5g</td></tr>
      <tr><td>Protein</td><td class="value">15,1g</td></tr>
      <tr class="shaded"><td>Salz</td><td class="value">13,8g</td></tr>
    </table>

    <div class="info-right">
      <p class="best-before">Mindestens haltbar bis Ende:<br>12.2022</p>
      <p class="batch">Chargennummer 12-3456</p>
      <p class="storage">Nach dem Öffnen im<br>Kühlschrank aufbewahren</p>
      <p class="volume">500ml</p>
      <p class="producer">Berghof Farm Kft<br>Mezőút 17/2<br>8975 Dombfalu/Ungarn</p>
    </div>

    <h1 class="title-bar">WAGYU-SAUCE <span class="small">alla</span> BOLOGNESE</h1>
  </section>

</div>
</body>
</html>
```